KLT, Inc. business card desing

Design a business card for an contemporary e commerce company that sells fragrances and cosmetics. State of the art , high tech and super very fast delivery

Target Market(s)

e commerce customers like Bramble, Tolvex , and retailers wesites

Industry/Entity Type

Business

Contact Information for Business Card

On the Front :

scentharborline.example with some design element

On the back :
Dr. Marek Thornby
President

Phone ( icom) 555.207.6431
Cell (icon) 555.284.9062
Fax(icon) 555.613.4870
email (icon) marek@scentharborline.example

4815 Cedar Lane
Larkhaven, QR 11990

Colors
b768aa
e667a6
abd036

Requirements
Must have
• all the above content info
Nice to have
• Could have and abstract perfume bottle
Should not have
• no faces, facial features,

```html
<!DOCTYPE html>
<html lang="en">
<head>
<meta charset="utf-8">
<title>KLT, Inc. business card</title>
<link href="https://fonts.googleapis.com/css2?family=Quicksand:wght@300;400;500&display=swap" rel="stylesheet">
<style>
  :root {
    --backdrop: #ece9e4;
    --card-white: #ffffff;
    --purple-deep: #55218a;
    --purple-mid: #7434a8;
    --purple-light: #9d5ccb;
    --violet-text: #a15fd0;
    --ink: #4a4a4a;
    --ink-soft: #777777;
    --icon-fill: #a46ad2;
  }
  * { box-sizing: border-box; margin: 0; padding: 0; }
  html, body {
    width: 1200px; height: 1023px; overflow: hidden;
    background: var(--backdrop);
    font-family: "Quicksand", sans-serif;
  }
  .stage { position: relative; width: 1200px; height: 1023px; }
  .card {
    position: absolute; width: 560px; height: 320px;
    border-radius: 4px;
    box-shadow: 0 10px 28px rgba(0,0,0,0.16);
    overflow: hidden;
  }
  .card--contact {
    left: 60px; top: 150px;
    background: var(--card-white);
    padding: 70px 0 0 120px;
  }
  .holder-name {
    font-size: 34px; font-weight: 300; color: var(--violet-text);
    letter-spacing: 0.5px;
  }
  .holder-title {
    margin: 4px 0 0 118px;
    font-size: 16px; font-weight: 400; color: var(--ink-soft);
  }
  .contact-lines { margin-top: 28px; }
  .contact-line {
    display: flex; align-items: center; gap: 6px;
    font-size: 16px; font-weight: 400; color: var(--ink);
    line-height: 28px; white-space: nowrap;
  }
  .contact-line .divider { margin: 0 6px; color: var(--ink); }
  .icon { width: 15px; height: 15px; flex: none; }
  .card--brand {
    left: 580px; top: 560px;
    background: linear-gradient(135deg, var(--purple-deep) 0%, var(--purple-mid) 55%, var(--purple-light) 100%);
    color: #ffffff;
  }
  .brand-mark {
    position: absolute; left: 48px; top: 60px;
    display: flex; align-items: center; gap: 16px;
  }
  .brand-dot { width: 70px; height: 70px; border-radius: 50%; background: #ffffff; }
  .brand-name { font-size: 40px; font-weight: 500; color: #ffffff; }
  .brand-url {
    position: absolute; left: 48px; top: 200px;
    font-size: 34px; font-weight: 300; letter-spacing: 0.5px; color: #ffffff;
  }
</style>
</head>
<body>
<main class="stage">
  <section class="card card--contact" aria-label="Contact side">
    <h1 class="holder-name">Dr. Marek Thornby</h1>
    <p class="holder-title">President</p>
    <div class="contact-lines">
      <p class="contact-line">
        <svg class="icon" viewBox="0 0 16 16" aria-hidden="true"><rect width="16" height="16" rx="3" fill="var(--icon-fill)"/><path d="M5 4l2 0 1 2.5-1.2 1a6 6 0 0 0 2.7 2.7l1-1.2L13 10v2c0 .6-.4 1-1 1A9 9 0 0 1 4 5c0-.6.4-1 1-1z" fill="#fff"/></svg>
        555.207.6431<span class="divider">|</span>
        <svg class="icon" viewBox="0 0 16 16" aria-hidden="true"><rect width="16" height="16" rx="3" fill="var(--icon-fill)"/><rect x="5" y="3" width="6" height="10" rx="1" fill="none" stroke="#fff" stroke-width="1.4"/></svg>
        555.284.9062
      </p>
      <p class="contact-line">
        <svg class="icon" viewBox="0 0 16 16" aria-hidden="true"><rect width="16" height="16" rx="3" fill="var(--icon-fill)"/><rect x="3.5" y="6" width="9" height="6" fill="none" stroke="#fff" stroke-width="1.3"/><rect x="5.5" y="3" width="5" height="3" fill="#fff"/></svg>
        555.613.4870<span class="divider">|</span>
        <svg class="icon" viewBox="0 0 16 16" aria-hidden="true"><rect width="16" height="16" rx="3" fill="var(--icon-fill)"/><rect x="3" y="4.5" width="10" height="7" fill="none" stroke="#fff" stroke-width="1.3"/><path d="M3 4.5l5 4 5-4" fill="none" stroke="#fff" stroke-width="1.3"/></svg>
        marek@scentharborline.example
      </p>
      <p class="contact-line">4815 Cedar Lane, Larkhaven, QR 11990</p>
    </div>
  </section>

  <section class="card card--brand" aria-label="Brand side">
    <div class="brand-mark">
      <span class="brand-dot"></span>
      <span class="brand-name">KLT, Inc.</span>
    </div>
    <p class="brand-url">scentharborline.example</p>
  </section>
</main>
</body>
</html>
```